Luxury Business Card Design

We need a business card design for a law firm that look sophisticated and luxury

Target Market(s)

Australian legal markets

Industry/Entity Type

Legal

Contact Information for Business Card

Attached

Requirements
Must have
• Logo, head office address on front side and 2 other addresses on the back side.
Nice to have
• Please see below our current business card. Need something more sophisticated and luxury feel

```html
<!DOCTYPE html>
<html lang="en">
<head>
<meta charset="utf-8">
<title>Ashcombe Lawyers – Business Cards</title>
<link href="https://fonts.googleapis.com/css2?family=Cinzel:wght@400;600&family=Montserrat:wght@400;500&display=swap" rel="stylesheet">
<style>
  :root {
    --page-bg: #2a2a2a;
    --card-bg: #1c1c1c;
    --gold: #c9a066;
    --gold-muted: #8c7350;
  }
  * { margin: 0; padding: 0; box-sizing: border-box; }
  html, body { width: 1200px; height: 1200px; overflow: hidden; background: var(--page-bg); }
  .canvas { position: relative; width: 1200px; height: 1200px; }
  .card {
    position: absolute; left: 263px; width: 675px; height: 385px;
    background: var(--card-bg);
    border: 2px solid var(--gold);
    color: var(--gold);
    font-family: "Montserrat", sans-serif;
  }
  .card--front { top: 153px; }
  .card--back { top: 637px; }
  .brand-ring {
    position: absolute; left: 50%; transform: translateX(-50%);
    border: 3px solid var(--gold); border-radius: 50%;
  }
  .card--front .brand-ring { top: 36px; width: 106px; height: 106px; }
  .card--back .brand-ring { top: 47px; width: 98px; height: 98px; }
  .brand-name {
    position: absolute; left: 0; right: 0; text-align: center;
    font-family: "Cinzel", serif; font-weight: 600; font-size: 44px; line-height: 1;
    letter-spacing: 0;
  }
  .card--front .brand-name { top: 161px; }
  .card--back .brand-name { top: 162px; }
  .brand-sub {
    position: absolute; left: 0; right: 0; display: flex; justify-content: center; align-items: center; gap: 10px;
    font-family: "Cinzel", serif; font-size: 15px; letter-spacing: 10px; line-height: 1;
  }
  .brand-sub::before, .brand-sub::after { content: ""; width: 30px; height: 1.5px; background: var(--gold); }
  .brand-sub span { margin-right: -10px; }
  .brand-sub { top: 211px; }
  .office-heading { font-family: "Cinzel", serif; font-size: 19px; letter-spacing: 1px; line-height: 1; }
  .office--melbourne {
    position: absolute; left: 30px; width: 245px; top: 262px; text-align: center;
    color: var(--gold-muted); font-size: 13.5px; line-height: 17px;
  }
  .office--melbourne .office-heading { margin-bottom: 4px; }
  .divider { position: absolute; left: 315px; top: 266px; width: 1px; height: 88px; background: var(--gold-muted); }
  .office--brisbane { position: absolute; left: 360px; top: 268px; font-size: 14px; }
  .office--brisbane .office-heading { margin-left: 22px; margin-bottom: 6px; font-size: 19px; }
  .contact-row { display: flex; align-items: center; gap: 6px; white-space: nowrap; }
  .contact-row svg { flex: none; }
  .address-block { display: flex; gap: 6px; margin-top: 6px; font-size: 12.5px; line-height: 15px; }
  .inline-phone { display: inline-flex; align-items: center; gap: 4px; }
  .person {
    position: absolute; left: 60px; top: 268px; color: var(--gold-muted);
  }
  .person-name { font-family: "Cinzel", serif; font-size: 25px; line-height: 1; }
  .person-title { font-size: 11.5px; margin-top: 3px; }
  .person .contact-row { font-size: 14.5px; margin-top: 7px; }
  .person .contact-row:first-of-type { margin-top: 11px; }
  .office--perth {
    position: absolute; left: 350px; width: 260px; top: 262px; text-align: center;
    font-size: 14px; line-height: 17px;
  }
  .office--perth .contact-row { justify-content: center; margin-top: 3px; font-size: 14px; }
</style>
</head>
<body>
<div class="canvas">

  <section class="card card--front">
    <div class="brand-ring"></div>
    <div class="brand-name">ASHCOMBE</div>
    <div class="brand-sub"><span>LAWYERS</span></div>

    <div class="office office--melbourne">
      <div class="office-heading">MELBOURNE</div>
      <div>Suite 410, Carrow Chambers</div>
      <div>212 Harlow Lane</div>
      <div>MELBOURNE, VIC 3000</div>
      <div class="inline-phone">
        <svg width="14" height="14" viewBox="0 0 24 24" fill="currentColor" aria-hidden="true"><path d="M6.6 10.8a15.1 15.1 0 0 0 6.6 6.6l2.2-2.2c.3-.3.7-.4 1-.2 1.1.4 2.3.6 3.6.6.6 0 1 .4 1 1V20c0 .6-.4 1-1 1A17 17 0 0 1 3 4c0-.6.4-1 1-1h3.5c.6 0 1 .4 1 1 0 1.3.2 2.5.6 3.6.1.3 0 .7-.2 1z"/></svg>
        +61 03 9000 1234
      </div>
    </div>

    <div class="divider"></div>

    <div class="office office--brisbane">
      <div class="office-heading">Brisbane</div>
      <div class="contact-row">
        <svg width="16" height="16" viewBox="0 0 24 24" fill="currentColor" aria-hidden="true"><path d="M6.6 10.8a15.1 15.1 0 0 0 6.6 6.6l2.2-2.2c.3-.3.7-.4 1-.2 1.1.4 2.3.6 3.6.6.6 0 1 .4 1 1V20c0 .6-.4 1-1 1A17 17 0 0 1 3 4c0-.6.4-1 1-1h3.5c.6 0 1 .4 1 1 0 1.3.2 2.5.6 3.6.1.3 0 .7-.2 1z"/></svg>
        +61 7 3000 5678
      </div>
      <div class="address-block">
        <svg width="16" height="20" viewBox="0 0 24 30" fill="none" stroke="currentColor" stroke-width="2.5" aria-hidden="true"><path d="M12 28S3 17 3 11a9 9 0 0 1 18 0c0 6-9 17-9 17z"/><circle cx="12" cy="11" r="3.5"/></svg>
        <div>Level 3, Ashcombe House,<br>88 Belmont Terrace, Spring Hill, QLD 4000</div>
      </div>
    </div>
  </section>

  <section class="card card--back">
    <div class="brand-ring"></div>
    <div class="brand-name">ASHCOMBE</div>
    <div class="brand-sub"><span>LAWYERS</span></div>

    <div class="person">
      <div class="person-name">Dr Elena Varga</div>
      <div class="person-title">Senior Migration Consultant (MARN#1234567)</div>
      <div class="contact-row">
        <svg width="15" height="11" viewBox="0 0 24 16" fill="none" stroke="currentColor" stroke-width="2" aria-hidden="true"><rect x="1" y="1" width="22" height="14"/><path d="M1 1l11 8 11-8"/></svg>
        elena@ashcombelawyers.com.au
      </div>
      <div class="contact-row">
        <svg width="15" height="16" viewBox="0 0 16 24" fill="none" stroke="currentColor" stroke-width="2" aria-hidden="true"><rect x="3" y="1" width="10" height="22" rx="1.5"/><path d="M6 19h4"/></svg>
        +61 0400 111 222
      </div>
    </div>

    <div class="office office--perth">
      <div>Suite 12,</div>
      <div>40 Marlow Highway</div>
      <div>NEDLANDS WA 6009</div>
      <div class="contact-row">
        <svg width="14" height="14" viewBox="0 0 24 24" fill="none" stroke="currentColor" stroke-width="2" aria-hidden="true"><circle cx="12" cy="12" r="10"/><path d="M2 12h20M12 2c3 3 3 17 0 20M12 2c-3 3-3 17 0 20"/></svg>
        www.ashcombelawyers.com.au
      </div>
      <div class="contact-row">
        <svg width="15" height="15" viewBox="0 0 24 24" fill="currentColor" aria-hidden="true"><path d="M6.6 10.8a15.1 15.1 0 0 0 6.6 6.6l2.2-2.2c.3-.3.7-.4 1-.2 1.1.4 2.3.6 3.6.6.6 0 1 .4 1 1V20c0 .6-.4 1-1 1A17 17 0 0 1 3 4c0-.6.4-1 1-1h3.5c.6 0 1 .4 1 1 0 1.3.2 2.5.6 3.6.1.3 0 .7-.2 1z"/></svg>
        +61 08 6000 3344
      </div>
    </div>
  </section>

</div>
</body>
</html>
```